Velmora Biz Card 2019

New business card for Velmora Property Inspections. We are a residential home inspection company in Arizona.

Target Market(s)

Real Estate

Font styles to use
Sans Serif

Requirements
Must have
• Glen Mirewick
• Home Inspector
• Velmora Property Inspections, LLC
• 480-555-0172
• glen@velmora-llc.example

```html
<!DOCTYPE html>
<html lang="en">
<head>
<meta charset="utf-8">
<title>Velmora Property Inspections – Business Card</title>
<link href="https://fonts.googleapis.com/css2?family=Open+Sans:ital,wght@0,400;0,600;1,400&display=swap" rel="stylesheet">
<style>
  :root {
    --page-bg: #080808;
    --card-bg: #252525;
    --card-bg-edge: #1b1b1b;
    --text-light: #ffffff;
    --text-muted: #d9d9d9;
    --brand-green: #4bb749;
  }
  * { box-sizing: border-box; margin: 0; padding: 0; }
  html, body {
    width: 1200px;
    height: 1000px;
    overflow: hidden;
    background: var(--page-bg);
    font-family: "Open Sans", Arial, sans-serif;
    color: var(--text-light);
  }
  .business-card {
    position: absolute;
    left: 16px;
    top: 109px;
    width: 1168px;
    height: 782px;
    background: radial-gradient(ellipse at 55% 45%, var(--card-bg) 0%, var(--card-bg-edge) 100%);
  }
  .brand-block {
    position: absolute;
    left: 91px;
    top: 300px;
    width: 348px;
    text-align: center;
  }
  .brand-name {
    font-weight: 600;
    font-size: 48px;
    letter-spacing: 8px;
    line-height: 1;
    padding-left: 8px;
    color: var(--text-light);
  }
  .brand-rule {
    margin-top: 20px;
    height: 4px;
    background: var(--brand-green);
  }
  .person-name {
    margin-top: 22px;
    font-size: 28px;
    font-weight: 600;
    line-height: 1.2;
  }
  .person-role {
    margin-top: 4px;
    font-size: 22px;
    font-weight: 400;
    color: var(--text-muted);
  }
  .company-title {
    position: absolute;
    left: 534px;
    top: 134px;
    font-size: 40px;
    font-weight: 400;
    line-height: 54px;
  }
  .title-rule {
    position: absolute;
    left: 534px;
    top: 255px;
    width: 347px;
    height: 3px;
    background: var(--brand-green);
  }
  .contact-list {
    position: absolute;
    left: 534px;
    top: 300px;
    list-style: none;
  }
  .contact-item {
    display: flex;
    align-items: center;
    height: 64px;
    margin-bottom: 51px;
    font-size: 41px;
    white-space: nowrap;
  }
  .contact-icon {
    width: 64px;
    height: 64px;
    margin-right: 16px;
    flex: none;
  }
  .tagline-band {
    position: absolute;
    left: 0;
    top: 641px;
    width: 100%;
    height: 66px;
    background: var(--brand-green);
    display: flex;
    align-items: center;
    justify-content: center;
  }
  .tagline {
    font-style: italic;
    font-size: 33px;
    padding-left: 68px;
  }
</style>
</head>
<body>
  <div class="business-card">
    <div class="brand-block">
      <div class="brand-name">VELMORA</div>
      <div class="brand-rule"></div>
      <p class="person-name">Glen Mirewick</p>
      <p class="person-role">Home Inspector</p>
    </div>

    <h1 class="company-title">Velmora Property<br>Inspections, LLC</h1>
    <div class="title-rule"></div>

    <ul class="contact-list">
      <li class="contact-item">
        <svg class="contact-icon" viewBox="0 0 64 64" aria-hidden="true">
          <circle cx="32" cy="32" r="30" fill="none" stroke="#fff" stroke-width="3"/>
          <path d="M22 17c2-1 4-1 5 1l3 6c1 2 0 3-1 4l-2 2c1 4 5 8 9 10l2-2c1-1 3-2 4-1l6 3c2 1 2 3 1 5l-2 3c-2 2-5 2-8 1-9-4-17-12-20-21-1-3 0-6 2-8z" fill="#fff"/>
        </svg>
        <span>480-555-0172</span>
      </li>
      <li class="contact-item">
        <svg class="contact-icon" viewBox="0 0 64 64" aria-hidden="true">
          <circle cx="32" cy="32" r="30" fill="none" stroke="#fff" stroke-width="3"/>
          <rect x="17" y="22" width="30" height="21" rx="2" fill="#fff"/>
          <path d="M18 24l14 11 14-11" fill="none" stroke="#252525" stroke-width="2.5"/>
        </svg>
        <span>glen@velmora-llc.example</span>
      </li>
      <li class="contact-item">
        <svg class="contact-icon" viewBox="0 0 64 64" aria-hidden="true">
          <circle cx="32" cy="32" r="30" fill="none" stroke="#fff" stroke-width="3"/>
          <g fill="none" stroke="#fff" stroke-width="2">
            <circle cx="32" cy="32" r="16"/>
            <ellipse cx="32" cy="32" rx="7" ry="16"/>
            <line x1="32" y1="16" x2="32" y2="48"/>
            <line x1="16" y1="32" x2="48" y2="32"/>
            <path d="M19 23h26M19 41h26"/>
          </g>
        </svg>
        <span>www.velmora-llc.example</span>
      </li>
    </ul>

    <div class="tagline-band">
      <p class="tagline">Helping Protect Your Family, Home, Investment</p>
    </div>
  </div>
</body>
</html>
```